Naturopath Practitioner Card Design

I am a naturopath needing a design for a business card mainly to show that I am a naturopath and have some contact details to give to prospective clients. I am open minded about the design and what is on the second side of the card whether it just be some artwork or space for details, appointment times etc. Naturopathy is the practice of natural medicine that uses a holistic approach and incorporates herbal and nutritional medicine.

Industry/Entity Type

Business

Contact Information for Business Card

Tom Welby NaturopathBHSc (Naturopathy) Member PHRA 0492 815 306 tom.welby@mailbright.com www.tomwelbynaturopathy.com.au

Requirements
Nice to have
• Would prefer some kind of original pattern/art work/logo rather than an image, not fussed if its very simple/basic
• I am open to any colour but think I would prefer a more earthy sandy clay etc type style than the greens that are commonly associated with naturopathy.
Should not have
• Don't really want to have generic stock images on it

```html
<!DOCTYPE html>
<html lang="en">
<head>
<meta charset="utf-8">
<title>Tom Welby Naturopathy – Business Card</title>
<link rel="stylesheet" href="https://fonts.googleapis.com/css2?family=Open+Sans:wght@400;600;700&display=swap">
<style>
  :root {
    --backdrop: #2b2b2d;
    --card-white: #ffffff;
    --ink: #1a1a1a;
    --rule: #3a3a3a;
    --photo-light: #c9c7c4;
    --photo-mid: #9b9793;
    --photo-dark: #6e6761;
    --text-light: #ffffff;
  }
  * { margin: 0; padding: 0; box-sizing: border-box; }
  html, body {
    width: 1200px; height: 900px; overflow: hidden;
    background: var(--backdrop);
    font-family: "Open Sans", Arial, sans-serif;
  }
  .stage { position: relative; width: 1200px; height: 900px; }

  .card {
    position: absolute;
    width: 580px; height: 332px;
    box-shadow: 0 10px 28px rgba(0,0,0,.45);
    overflow: hidden;
  }

  .card-title {
    font-family: "Open Sans", Arial, sans-serif;
    font-weight: 600;
    line-height: 1;
    letter-spacing: .2px;
  }

  /* Back: appointment side */
  .card--back { left: 110px; top: 90px; background: var(--card-white); color: var(--ink); }
  .back-brand { position: absolute; right: 40px; top: 32px; text-align: right; }
  .back-brand .card-title { font-size: 38px; color: var(--ink); }
  .back-brand .membership { font-size: 16px; margin-top: 6px; letter-spacing: .3px; }

  .appointment { position: absolute; left: 40px; top: 150px; right: 70px; }
  .appointment-label { font-size: 15px; letter-spacing: .5px; margin-bottom: 10px; }
  .field { display: flex; align-items: flex-end; height: 44px; font-size: 16px; }
  .field-label { white-space: nowrap; padding-right: 4px; }
  .field-line { flex: 1; border-bottom: 1.5px solid var(--rule); margin-bottom: 5px; }

  /* Front: practitioner side */
  .card--front { left: 510px; top: 478px; color: var(--text-light); }
  .front-photo {
    position: absolute; inset: 0;
    background:
      radial-gradient(ellipse at 40% 75%, var(--photo-dark) 0%, transparent 45%),
      radial-gradient(ellipse at 75% 30%, #a69c8c 0%, transparent 40%),
      linear-gradient(160deg, var(--photo-light) 0%, var(--photo-mid) 60%, #8a8580 100%);
  }
  .front-title {
    position: absolute; left: 110px; top: 46px;
    font-size: 50px; color: var(--text-light);
  }
  .practitioner { position: absolute; right: 28px; top: 150px; text-align: right; }
  .practitioner-name { font-size: 22px; font-weight: 700; letter-spacing: .5px; }
  .practitioner-title {
    font-size: 12px; letter-spacing: .6px;
    border-bottom: 1.5px solid var(--text-light);
    padding: 0 0 3px 40px;
  }
  .contact-rule {
    position: absolute; left: 0; right: 130px; top: 252px;
    border-top: 1.5px solid var(--text-light);
  }
  .contact { position: absolute; left: 24px; top: 264px; font-size: 15px; line-height: 1.5; }
  .contact-row { display: flex; align-items: center; gap: 8px; }
  .contact-row svg { width: 12px; height: 12px; fill: var(--text-light); }
</style>
</head>
<body>
<main class="stage">

  <section class="card card--back" aria-label="Appointment side of business card">
    <div class="back-brand">
      <h2 class="card-title">Naturopathy</h2>
      <p class="membership">Member PHRA</p>
    </div>
    <div class="appointment">
      <p class="appointment-label">APPOINTMENT</p>
      <div class="field"><span class="field-label">Name:</span><span class="field-line"></span></div>
      <div class="field"><span class="field-label">Time:</span><span class="field-line"></span></div>
      <div class="field"><span class="field-label">Date:</span><span class="field-line"></span></div>
    </div>
  </section>

  <section class="card card--front" aria-label="Practitioner side of business card">
    <div class="front-photo" role="img" aria-label="Photo of a wooden mortar and pestle with chamomile flowers, a stethoscope and brass scales on a soft grey background"></div>
    <h1 class="card-title front-title">Naturopathy</h1>
    <div class="practitioner">
      <p class="practitioner-name">TOM WELBY</p>
      <p class="practitioner-title">NATUROPATH (BHSC)</p>
    </div>
    <div class="contact-rule"></div>
    <div class="contact">
      <p class="contact-row">
        <svg viewBox="0 0 24 24" aria-hidden="true"><path d="M6.6 10.8a15.1 15.1 0 0 0 6.6 6.6l2.2-2.2a1 1 0 0 1 1-.25 11.4 11.4 0 0 0 3.6.57 1 1 0 0 1 1 1V20a1 1 0 0 1-1 1A17 17 0 0 1 3 4a1 1 0 0 1 1-1h3.5a1 1 0 0 1 1 1c0 1.25.2 2.45.57 3.57a1 1 0 0 1-.25 1z"/></svg>
        0492 815 306
      </p>
      <p class="contact-row">
        <svg viewBox="0 0 24 24" aria-hidden="true"><path d="M2 5h20v14H2z M4 7v.5l8 5 8-5V7z" fill-rule="evenodd"/></svg>
        tom.welby@mailbright.com
      </p>
    </div>
  </section>

</main>
</body>
</html>
```